online jewellery store business card

all black business card, glossy, with gold writing, gold logo and name (provided). simple design.

Target Market(s)

This business card is to put with purchases, so it just needs the logo and name Solvane Jewellery which I have uploaded pictures for you to use. Then it needs the web address, markolo address, email address and then the like us on CH for 10% off. All words to be used have been provided. Thanks

Industry/Entity Type

Store

Contact Information for Business Card

www.solvanejewellery.com
stores.markolo.com.au/Solvane-Jewellery
info@solvanejewellery.com

Like us on chatterly for 10% off your next purchase!

Requirements
Must have
• black background
gold writing
glossy look
Should not have
• yellow writing

```html
<!DOCTYPE html>
<html lang="en">
<head>
<meta charset="utf-8">
<title>Solvane Jewellery – Business Card</title>
<link rel="stylesheet" href="https://fonts.googleapis.com/css2?family=Cabin+Condensed:wght@400&family=Raleway:wght@400&family=Encode+Sans+Semi+Condensed:wght@300&display=swap">
<style>
  :root {
    --card-black: #050607;
    --card-sheen: #2b3131;
    --gold: #d2b56f;
    --gold-deep: #b08a3c;
    --gold-ring: #6f6542;
  }
  * { margin: 0; padding: 0; box-sizing: border-box; }
  html, body {
    width: 1200px;
    height: 693px;
    overflow: hidden;
    background: var(--card-black);
  }
  .card {
    position: relative;
    width: 1200px;
    height: 693px;
    overflow: hidden;
    background:
      radial-gradient(ellipse 520px 620px at 1200px 330px, var(--card-sheen) 0%, rgba(43,49,49,0.35) 45%, rgba(5,6,7,0) 80%),
      linear-gradient(180deg, #0a0b0c 0%, var(--card-black) 100%);
  }
  .brand-ring {
    position: absolute;
    left: 144px;
    top: 60px;
    width: 214px;
    height: 214px;
  }
  .brand-name {
    position: absolute;
    left: 51px;
    width: 400px;
    text-align: center;
    font-family: "Raleway", sans-serif;
    font-weight: 400;
    color: var(--gold);
    line-height: 1;
    white-space: nowrap;
  }
  .brand-name--first { top: 292px; font-size: 52px; letter-spacing: 0.2em; padding-left: 0.2em; }
  .brand-name--second { top: 364px; font-size: 48px; letter-spacing: 0.17em; padding-left: 0.17em; }
  .offer {
    position: absolute;
    left: 503px;
    top: 160px;
    width: 620px;
    text-align: center;
    font-family: "Cabin Condensed", sans-serif;
    font-weight: 400;
    font-size: 60px;
    line-height: 71px;
    letter-spacing: 0.05em;
    color: var(--gold);
  }
  .contact {
    position: absolute;
    left: 243px;
    width: 700px;
    text-align: center;
    font-family: "Encode Sans Semi Condensed", sans-serif;
    font-weight: 300;
    font-size: 33px;
    line-height: 1;
    letter-spacing: 0.04em;
    color: var(--gold-deep);
    white-space: nowrap;
  }
  .contact--web { top: 479px; }
  .contact--store { top: 515px; }
  .contact--email { top: 585px; color: var(--gold); }
</style>
</head>
<body>
  <main class="card">
    <svg class="brand-ring" viewBox="0 0 214 214" aria-hidden="true">
      <circle cx="107" cy="107" r="104" fill="none" stroke="var(--gold-ring)" stroke-width="2"/>
    </svg>
    <div class="brand-name brand-name--first">SOLVANE</div>
    <div class="brand-name brand-name--second">JEWELLERY</div>

    <p class="offer">Like us on<br>chatterly for 10%<br>off your next purchase!</p>

    <p class="contact contact--web">www.solvanejewellery.com</p>
    <p class="contact contact--store">stores.markolo.com.au/Solvane-Jewellery</p>
    <p class="contact contact--email">email:info@solvanejewellery.com</p>
  </main>
</body>
</html>
```